Ferncrest Dental, LLC business card project

Business card to be designed with current logo.
Dental office- please keep design of card that looks clean and professional.
Please include the following info:
Ferncrest Dental, LLC
Dr. Lorna Pettigrew
2871 Marlowe Street
Bethlehem, PA 18093
610-555-0193
ferncrestdental.office@examplemail.test
Hello everyone-
Reason: Just got back from overseas- will look at all designs and provide feedback. Thank you!
Reason: Polling my friends for the final selection-
thank you to all those that participated- so many talented designers!

```html
<!DOCTYPE html>
<html lang="en">
<head>
<meta charset="utf-8">
<title>Ferncrest Dental, LLC — Business Card</title>
<link rel="stylesheet" href="https://fonts.googleapis.com/css2?family=Arimo:wght@400&display=swap">
<style>
  :root {
    --card-bg: #ffffff;
    --brand-green: #5cc31a;
    --brand-lime: #9be31d;
    --wash-green: #f1fbe2;
    --wash-green-soft: #f8fdf0;
    --name-ink: #1c1c1c;
    --body-ink: #4a4a4a;
  }
  html, body {
    margin: 0;
    padding: 0;
    width: 1200px;
    height: 687px;
    overflow: hidden;
    background: var(--card-bg);
  }
  .card {
    position: relative;
    width: 1200px;
    height: 687px;
    background: var(--card-bg);
    font-family: "Arimo", Arial, sans-serif;
    overflow: hidden;
  }
  .backdrop {
    position: absolute;
    left: 0;
    top: 200px;
    width: 980px;
    height: 450px;
  }
  .brand {
    position: absolute;
    left: 114px;
    top: 98px;
    display: flex;
    align-items: center;
    gap: 26px;
  }
  .brand-dot {
    width: 58px;
    height: 58px;
    border-radius: 50%;
    background: var(--brand-green);
  }
  .brand-name {
    margin: 0;
    font-size: 66px;
    font-weight: 400;
    line-height: 1;
    color: var(--brand-green);
    letter-spacing: -0.5px;
  }
  .details {
    position: absolute;
    left: 746px;
    transform: translateX(-50%);
    text-align: center;
    white-space: nowrap;
    color: var(--body-ink);
  }
  .doctor {
    top: 254px;
    margin: 0;
    font-size: 40px;
    font-weight: 400;
    color: var(--name-ink);
  }
  .contact {
    top: 356px;
    margin: 0;
    font-style: normal;
    font-size: 34px;
    line-height: 50px;
  }
  .email {
    top: 480px;
    margin: 0;
    font-size: 31px;
  }
</style>
</head>
<body>
  <main class="card">
    <svg class="backdrop" viewBox="0 0 980 450" role="img" aria-label="Faint pale-green landscape decoration" xmlns="http://www.w3.org/2000/svg">
      <defs>
        <linearGradient id="wash" x1="0" y1="0" x2="1" y2="1">
          <stop offset="0" stop-color="var(--wash-green)"/>
          <stop offset="1" stop-color="var(--wash-green-soft)"/>
        </linearGradient>
      </defs>
      <path d="M0 450 L0 385 Q430 330 980 420 L980 450 Z" fill="url(#wash)"/>
    </svg>

    <header class="brand">
      <span class="brand-dot"></span>
      <h1 class="brand-name">Ferncrest Dental, LLC</h1>
    </header>

    <h2 class="details doctor">Dr. Lorna Pettigrew</h2>

    <address class="details contact">
      2871 Marlowe Street Bethlehem, PA 18093<br>
      610-555-0193
    </address>

    <p class="details email">ferncrestdental.office@examplemail.test</p>
  </main>
</body>
</html>
```